Tradeshow Banner Stand - 36" x 80

Create design for a new banner i will order.
- Training on how to "add on" Christmas Light Installation to your current Service Business.

at https://brightenyourseasonplan.example/live

sorry but my GM wants it to have these items- and be more simple (not so busy)

ATTN: LANDSCAPERS
Is Your Winter
Revenue Down?

Add On Christmas Light Install
with Lumavexa’s FREE Training

Benefits:
• Grow Winter Revenue
• High Profit Margin (30% plus)
• High Growth Industry
• Avoid Off-Season Layoffs
• Use Cashflow to Grow Biz

Learn More at www.LumavexaGlow.example – QR?

```html
<!DOCTYPE html>
<html lang="en">
<head>
<meta charset="utf-8">
<title>Attn: Landscapers – Is Your Winter Revenue Down?</title>
<link rel="stylesheet" href="https://fonts.googleapis.com/css2?family=Oswald:wght@500;600&family=Montserrat:wght@700&family=Roboto+Condensed:wght@400;700&display=swap">
<style>
  :root {
    --navy: #15203a;
    --navy-deep: #0e1628;
    --yellow: #f7e11b;
    --red: #e3261d;
    --white: #ffffff;
    --ink: #111111;
    --night-a: #3a2a1c;
    --night-b: #1a1f2b;
  }
  * { margin: 0; padding: 0; box-sizing: border-box; }
  html, body { width: 1200px; height: 2929px; overflow: hidden; background: var(--white); }
  .banner { position: relative; width: 1200px; height: 2929px; background: var(--white); overflow: hidden; }
  .panel {
    position: absolute; left: 32px; top: 32px; width: 1136px; height: 2500px;
    background: linear-gradient(180deg, var(--navy) 0%, var(--navy-deep) 55%, var(--navy) 100%);
  }
  .art { position: absolute; inset: 0; width: 1200px; height: 2929px; }
  .photo-house-top {
    position: absolute; left: 32px; top: 32px; width: 775px; height: 519px;
    clip-path: polygon(0 0, 100% 0, 0 100%);
    background: radial-gradient(ellipse at 30% 40%, #6a4a2a 0%, var(--night-a) 40%, var(--night-b) 100%);
  }
  .photo-house-mid {
    position: absolute; left: 148px; top: 950px; width: 1020px; height: 503px;
    clip-path: polygon(15.8% 0, 100% 0, 100% 78.5%, 0 100%);
    background: radial-gradient(ellipse at 50% 45%, #7a5530 0%, #3d2b1d 45%, #141a26 100%);
  }
  .headline { position: absolute; left: 0; width: 1200px; text-align: center; font-family: "Oswald", sans-serif; font-weight: 600; text-transform: uppercase; line-height: 1; white-space: nowrap; }
  .headline-lead { top: 398px; font-size: 84px; color: var(--white); }
  .headline-question { top: 486px; font-size: 128px; color: var(--yellow); }
  .headline-answer { top: 604px; font-size: 140px; color: var(--red); }
  .subhead { position: absolute; left: 0; width: 1200px; text-align: center; font-family: "Montserrat", sans-serif; font-weight: 700; font-size: 47px; color: var(--red); text-transform: uppercase; line-height: 60px; top: 768px; white-space: nowrap; }
  .benefits { position: absolute; left: 156px; top: 1530px; font-family: "Roboto Condensed", sans-serif; color: var(--white); }
  .benefits-title { font-weight: 700; font-size: 56px; color: var(--yellow); text-transform: uppercase; line-height: 1; margin-bottom: 40px; }
  .benefits-list { list-style: none; font-size: 54px; }
  .benefits-list li { height: 100px; line-height: 70px; padding-left: 42px; position: relative; }
  .benefits-list li::before { content: ""; position: absolute; left: 0; top: 28px; width: 16px; height: 16px; border-radius: 50%; background: var(--white); }
  .details { position: absolute; top: 2288px; font-family: "Roboto Condensed", sans-serif; color: var(--white); white-space: nowrap; }
  .details h3 { font-weight: 700; font-size: 38px; text-transform: uppercase; line-height: 1; margin-bottom: 30px; }
  .details p { font-size: 36px; line-height: 52px; }
  .details-site { left: 113px; }
  .details-live { left: 560px; }
  .divider { position: absolute; top: 2290px; left: 536px; width: 7px; height: 148px; background: var(--yellow); }
  .photo-house-foot {
    position: absolute; left: 80px; top: 2548px; width: 565px; height: 265px;
    background: linear-gradient(180deg, #b9c4cf 0%, #8a8074 55%, #3b3a33 100%);
  }
  .brand { position: absolute; left: 672px; top: 2548px; width: 460px; height: 265px; display: flex; align-items: center; justify-content: center; gap: 18px; white-space: nowrap; }
  .brand-dot { width: 38px; height: 38px; border-radius: 50%; background: var(--red); flex: none; }
  .brand-name { font-family: "Oswald", sans-serif; font-weight: 600; font-size: 56px; color: var(--red); }
  .foot-bar { position: absolute; left: 32px; top: 2830px; width: 1136px; height: 58px; background: var(--ink); }
</style>
</head>
<body>
<main class="banner">
  <div class="panel"></div>
  <div class="photo-house-top" role="img" aria-label="Night photo of a two-storey house outlined in warm white holiday lights"></div>
  <div class="photo-house-mid" role="img" aria-label="Night photo of a large home with trees and hedges wrapped in red and white holiday lights"></div>
  <svg class="art" viewBox="0 0 1200 2929" aria-hidden="true">
    <line x1="807" y1="32" x2="32" y2="551" stroke="#f7e11b" stroke-width="6"/>
    <line x1="1168" y1="842" x2="1000" y2="941" stroke="#f7e11b" stroke-width="6"/>
    <line x1="148" y1="1453" x2="1168" y2="1345" stroke="#0e1628" stroke-width="2"/>
    <polygon points="140,1452 232,1452 150,1486" fill="#e3261d"/>
    <line x1="110" y1="1494" x2="150" y2="1486" stroke="#f7e11b" stroke-width="5"/>
  </svg>

  <h1>
    <span class="headline headline-lead">Attn: Landscapers</span>
    <span class="headline headline-question">Is Your Winter</span>
    <span class="headline headline-answer">Revenue Down?</span>
  </h1>
  <h2 class="subhead">Add On Christmas Light Install<br>with Lumavexa’s FREE Training</h2>

  <section class="benefits">
    <h3 class="benefits-title">Benefits:</h3>
    <ul class="benefits-list">
      <li>Grow Winter Revenue</li>
      <li>High Profit Margin (30% plus)</li>
      <li>High Growth Industry</li>
      <li>Avoid Off-Season Layoffs</li>
      <li>Use Cashflow to Grow Biz</li>
    </ul>
  </section>

  <section class="details details-site"><h3>Learn More</h3><p>www.LumavexaGlow.example</p></section>
  <div class="divider"></div>
  <section class="details details-live"><h3>Free Live Training</h3><p>brightenyourseasonplan.example/live</p></section>

  <div class="photo-house-foot" role="img" aria-label="Dusk photo of a stone house trimmed with white holiday lights"></div>
  <div class="brand"><span class="brand-dot"></span><span class="brand-name">Lumavexa Lights</span></div>
  <div class="foot-bar"></div>
</main>
</body>
</html>
```